Business card design needed

see my website

www.calderwoodandpike.com

I am after a new logo and business card needs to fit in with the website. I like the look of typewriter text - would like this on the website as well if I could!

Industry/Entity Type

Business

Contact Information for Business Card

Calderwood and Pike
Design and Heritage Consultants

Marcia Dowell
Principal

+61 437 690 215
marcia@calderwoodandpike.com

www.calderwoodandpike.com

back of card

Interior Design
Consultancy on Period Home restoration and renovation
Heritage Impact Statements
Conservation Management Plans
Materials Conservation
Historical Research

```html
<!DOCTYPE html>
<html lang="en">
<head>
<meta charset="utf-8">
<title>Calderwood and Pike — Business Card</title>
<link href="https://fonts.googleapis.com/css2?family=Courier+Prime:wght@400;700&family=Arimo:wght@700&display=swap" rel="stylesheet">
<style>
  :root {
    --page: #ffffff;
    --teal: #62b9aa;
    --ink: #1d1d1d;
    --card-edge: #2a2a2a;
    --white: #ffffff;
  }
  * { margin: 0; padding: 0; box-sizing: border-box; }
  html, body {
    width: 849px; height: 1200px; overflow: hidden;
    background: var(--page);
  }
  .sheet { position: relative; width: 849px; height: 1200px; }
  .card {
    position: absolute; left: 105px; width: 659px; height: 405px;
    border: 1.5px solid var(--card-edge); background: var(--white);
    overflow: hidden;
  }
  .card--front { top: 232px; }
  .card--back { top: 659px; }

  .front__band {
    position: absolute; left: 0; top: 0; width: 226px; height: 100%;
    background: var(--teal);
  }
  .brand {
    position: absolute; left: 0; top: 118px; width: 100%; height: 36px;
    font-family: "Courier Prime", monospace; font-weight: 700;
    font-size: 28px; line-height: 36px; white-space: nowrap;
  }
  .brand__first {
    position: absolute; left: 0; width: 222px; text-align: right;
    color: var(--white);
  }
  .brand__rest {
    position: absolute; left: 234px;
    color: var(--ink);
  }
  .tagline {
    position: absolute; left: 230px; top: 152px;
    font-family: "Arimo", sans-serif; font-weight: 700;
    font-size: 13px; letter-spacing: 1.2px; color: #333;
    white-space: nowrap;
  }
  .mark-dot {
    position: absolute; left: 182px; top: 212px;
    width: 44px; height: 44px; border-radius: 50%;
    background: var(--ink);
  }
  .contact {
    position: absolute; left: 232px; top: 202px;
    font-family: "Courier Prime", monospace; white-space: nowrap;
  }
  .contact__name {
    color: var(--teal); font-weight: 700; font-size: 20px; line-height: 26px;
  }
  .contact__line {
    color: var(--ink); font-weight: 700; font-size: 13px; line-height: 17px;
  }

  .back__brand {
    position: absolute; left: 0; right: 0; top: 104px;
    text-align: center;
    font-family: "Courier Prime", monospace; font-weight: 700;
    font-size: 26px; color: var(--ink);
  }
  .services {
    position: absolute; left: 0; right: 0; top: 197px;
    text-align: center; list-style: none;
    font-family: "Courier Prime", monospace; font-weight: 400;
    font-size: 16px; line-height: 25.5px; color: var(--teal);
  }
</style>
</head>
<body>
<main class="sheet">
  <section class="card card--front" aria-label="Business card front">
    <div class="front__band"></div>
    <h1 class="brand"><span class="brand__first">Calderwood</span><span class="brand__rest">and Pike</span></h1>
    <p class="tagline">Design and Heritage Consultants</p>
    <span class="mark-dot" aria-hidden="true"></span>
    <div class="contact">
      <p class="contact__name">Marcia Dowell Principal</p>
      <p class="contact__line">Phone: +61 437 690 215</p>
      <p class="contact__line">marcia@calderwoodandpike.com</p>
      <p class="contact__line">www.calderwoodandpike.com</p>
    </div>
  </section>

  <section class="card card--back" aria-label="Business card back">
    <p class="back__brand">Calderwood and Pike</p>
    <ul class="services">
      <li>Interior Design Consultancy on Period</li>
      <li>Home restoration and renovation Heritage</li>
      <li>Impact Statements Conservation Management</li>
      <li>Plans Materials Conservation Historical</li>
      <li>Research</li>
    </ul>
  </section>
</main>
</body>
</html>
```